Flyer to advertise a starter pack bundle we are offering to student plumbers

We need sales flyer we have the images attached and is a part of a bundle that we sell to new students. this bundle will include ether the Harborline 312 image or the Vesta TR9 image. all other other items are included. we are in the plumbing trades industry.

Target Market(s)

blue collar trade, plumbers, sprinkler fitters, irrigation techs, backflow testers

Industry/Entity Type

plumbing, fire sprinkler, waterworks, irrigation

```html
<!DOCTYPE html>
<html lang="en">
<head>
<meta charset="UTF-8">
<title>Plumbing Trades Starter Bundle Flyer</title>
<link href="https://fonts.googleapis.com/css2?family=Poppins:wght@400;500;700;800&display=swap" rel="stylesheet">
<style>
  :root {
    --royal-blue: #0a2ea6;
    --amber: #eba00b;
    --ink: #0d1030;
    --paper: #ffffff;
    --panel-grey: #e8e7ea;
    --backdrop: #ebe9ea;
  }
  * { margin: 0; padding: 0; box-sizing: border-box; }
  html, body {
    width: 1200px;
    height: 1200px;
    overflow: hidden;
    background: var(--backdrop);
    font-family: "Poppins", sans-serif;
  }
  .flyer {
    position: absolute;
    left: 151px;
    top: 20px;
    width: 1066px;
    height: 1377px;
    background: var(--paper);
    transform: scale(0.8424);
    transform-origin: top left;
    overflow: hidden;
  }
  .hero-photo {
    position: absolute;
    left: 0; top: 0;
    width: 1066px; height: 590px;
    background:
      radial-gradient(ellipse 170px 120px at 800px 110px, rgba(236,140,40,0.85) 0%, rgba(236,140,40,0) 100%),
      radial-gradient(ellipse 230px 300px at 800px 420px, rgba(40,80,160,0.9) 0%, rgba(40,80,160,0) 100%),
      linear-gradient(90deg, #4f5862 0%, #6f767f 30%, #5a5d62 45%, #7a6348 60%, #9a7f5c 80%, #5a4f44 100%);
  }
  .hero-shapes {
    position: absolute;
    left: 0; top: 0;
    width: 1066px; height: 600px;
  }
  .title-box {
    position: absolute;
    left: 67px; top: 292px;
    width: 580px; height: 289px;
    background: var(--royal-blue);
    padding: 40px 0 0 39px;
  }
  .title-box h1 {
    color: var(--paper);
    font-weight: 700;
    font-size: 42px;
    line-height: 53px;
    letter-spacing: 0.2px;
  }
  .intro {
    position: absolute;
    left: 69px; top: 610px;
    white-space: nowrap;
    font-size: 22px;
    line-height: 28px;
    letter-spacing: 0.35px;
    color: var(--ink);
    text-transform: uppercase;
  }
  .intro strong { font-weight: 700; }
  .section-bar {
    position: absolute;
    left: 84px; top: 724px;
    width: 448px; height: 52px;
    background: var(--royal-blue);
    color: var(--paper);
    font-weight: 700;
    font-size: 29px;
    line-height: 52px;
    padding-left: 59px;
  }
  .product-photo {
    position: absolute;
    background: linear-gradient(160deg, #efeef0 0%, #dedde1 100%);
  }
  .product-photo.harborline {
    left: 131px; top: 776px; width: 358px; height: 238px;
    background:
      radial-gradient(ellipse 120px 90px at 180px 120px, #8f9194 0%, rgba(143,145,148,0) 100%),
      linear-gradient(160deg, #efeef0 0%, #e3e2e5 100%);
  }
  .product-photo.vesta {
    left: 131px; top: 1066px; width: 358px; height: 203px;
    background:
      radial-gradient(ellipse 110px 80px at 200px 120px, #4fd4e4 0%, rgba(79,212,228,0) 100%),
      linear-gradient(160deg, #efeef0 0%, #e3e2e5 100%);
  }
  .product-photo.kit {
    left: 536px; top: 825px; width: 530px; height: 177px;
    background:
      radial-gradient(ellipse 140px 90px at 250px 80px, #4a4a48 0%, rgba(74,74,72,0) 100%),
      linear-gradient(180deg, var(--panel-grey) 0%, #e6e5e8 100%);
  }
  .product-label {
    position: absolute;
    left: 84px;
    width: 360px; height: 52px;
    background: var(--royal-blue);
    color: var(--paper);
    font-weight: 700;
    font-size: 28px;
    line-height: 52px;
    padding-left: 120px;
  }
  .product-label.first { top: 1014px; }
  .product-label.second { top: 1269px; }
  .accents {
    position: absolute;
    left: 0; top: 0;
    width: 1066px; height: 1377px;
    pointer-events: none;
  }
  .cta-heading {
    position: absolute;
    left: 562px; top: 1066px;
    font-size: 35px;
    font-weight: 700;
    color: var(--royal-blue);
    white-space: nowrap;
  }
  .cta-body {
    position: absolute;
    left: 587px; top: 1118px;
    white-space: nowrap;
    font-size: 22px;
    line-height: 28px;
    color: var(--ink);
  }
  .footer-band {
    position: absolute;
    left: 0; top: 1321px;
    width: 1066px; height: 56px;
    background: var(--amber);
  }
</style>
</head>
<body>
  <div class="flyer">
    <div class="hero-photo" role="img" aria-label="Smiling young tradesman in an orange hard hat and blue work jacket standing in an industrial plant beside electrical panels and pipework"></div>
    <svg class="hero-shapes" viewBox="0 0 1066 600" aria-hidden="true">
      <polygon points="0,384 1066,496 1066,584 0,430" fill="var(--amber)"/>
      <polygon points="0,430 1066,584 1066,600 0,600" fill="var(--paper)"/>
    </svg>

    <div class="title-box">
      <h1>GEAR UP FOR SUCCESS :<br>YOUR ESSENTIAL<br>PLUMBING TRADES<br>STARTER BUNDLE!</h1>
    </div>

    <p class="intro"><strong>Kickstart your plumbing career with confidence!</strong>&nbsp; This exclusive starter<br>bundle provides you with all the essential tools and resources you need<br>to hit the ground running in the exciting world of plumbing trades.</p>

    <div class="section-bar">HIGH-QUALITY TOOLS:</div>

    <div class="product-photo harborline" role="img" aria-label="Grey backflow test kit case with analog pressure gauge and red, yellow and blue hoses"></div>
    <div class="product-label first">HARBORLINE 312</div>

    <div class="product-photo vesta" role="img" aria-label="Turquoise digital backflow test gauge with hanging hook and hoses"></div>
    <div class="product-label second">VESTA TR9</div>

    <div class="product-photo kit" role="img" aria-label="Brass fittings and adapters in an open black foam-lined case with a clear sight tube and valve assembly"></div>

    <svg class="accents" viewBox="0 0 1066 1377" aria-hidden="true">
      <polygon points="489,776 532,776 489,819" fill="var(--amber)"/>
      <polygon points="84,1014 131,1014 131,969" fill="var(--amber)"/>
      <polygon points="84,1269 131,1269 131,1224" fill="var(--amber)"/>
    </svg>

    <h2 class="cta-heading">INVEST IN YOUR FUTURE!</h2>
    <p class="cta-body">DON'T WAIT &ndash;&nbsp; LAUNCH YOUR<br>PLUMBING CAREER EFFECTIVELY<br>WITH THIS SPECIALLY DESIGNED<br>STARTER BUNDLE.&nbsp; CONTACT US<br>TODAY TO LEARN MORE AND PLACE<br>YOUR ORDER!</p>

    <div class="footer-band"></div>
  </div>
</body>
</html>
```